Event Website Design

We need a new website design for an events driven website. The domain for this site is http://brackmoorhalls.co.uk. The site is up and running but needs a new fresh, modern look.
I've attached a Balamiq Mockup for the layout of the home page. Also attached is a png of the logo.
Key colours for the site are 0f7e6a, 35bde, d57835 & 373737.
Font to use is Proxima Nova
Width of the site should be 1200px
The design should be contemporary with minimal clutter.
Websites to references are…
http://vantora.london/
http://www.thekrd.co.uk/
These are just guidelines, please feel free to use you own creative judgment.
The selected design file needs to be supplied as an editable PSD.
Updates
Reason: I've submitted 5 designs to the client, who will select the one they want. I will then choose that design. So please be patient as I'm waiting for a decision from my client.
Industry/Entity Type
Events
Number of Pages Required
1 page
Look and feel
Each slider illustrates characteristics of the customer's brand and the style your logo design should communicate.

```html
<!DOCTYPE html>
<html lang="en">
<head>
<meta charset="utf-8">
<title>Brackmoor Halls – Home</title>
<link rel="stylesheet" href="https://fonts.googleapis.com/css2?family=Open+Sans:wght@400;600;700&display=swap">
<style>
:root{
  --ink:#2f2f2f;
  --header:#333333;
  --dark-band:#393939;
  --footer:#3a3a3a;
  --sky:#2bb4e8;
  --sun:#f8c95a;
  --teal:#1b9c7f;
  --teal-light:#3bbfa0;
  --link-blue:#3bbde0;
  --white:#ffffff;
  --mid-grey:#d9d9d9;
}
*{box-sizing:border-box;margin:0;padding:0}
html,body{width:1200px;height:3774px;overflow:hidden}
body{position:relative;background:var(--white);font-family:"Open Sans",Arial,sans-serif;color:var(--ink)}
.abs{position:absolute}
a{color:inherit;text-decoration:none}

/* top strip */
.social{top:10px;right:22px;display:flex;gap:8px}
.social span{display:block;width:26px;height:26px;border-radius:3px}
.social .s1{background:#3b5b99}.social .s2{background:#1da1e2}.social .s3{background:#3a8fc4}

/* header */
.site-header{top:45px;left:0;width:1200px;height:93px;background:var(--header)}
.brand{left:36px;top:30px;color:var(--white);font-weight:700;font-size:26px;letter-spacing:1px;display:flex;align-items:center;gap:10px;white-space:nowrap}
.brand i{display:block;width:16px;height:16px;background:var(--teal-light)}
.account-links{right:30px;top:18px;font-size:14px;font-weight:600;color:var(--link-blue);letter-spacing:.3px;white-space:nowrap}
.account-links span{margin-left:6px}
.account-links .on{color:var(--white)}
.box-office{right:30px;top:50px;color:var(--white);font-weight:700;font-size:28px;letter-spacing:.5px;white-space:nowrap}

/* nav */
.main-nav{top:138px;left:0;width:1200px;height:53px;display:flex;align-items:center;padding-left:34px;font-size:17px;font-weight:600;color:#444;white-space:nowrap}
.main-nav a{padding:0 6px;border-right:1px solid #999;line-height:18px}
.main-nav a:last-child{border-right:0}
.main-nav .current{color:var(--link-blue)}

/* hero */
.hero{top:191px;left:0;width:1200px;height:604px;background:linear-gradient(160deg,#c9c0b5 0%,#8b7c6e 40%,#5d4f45 75%,#3a302b 100%)}
.search{right:30px;top:35px;width:340px;height:38px;background:rgba(255,255,255,.85);border-radius:20px}
.search svg{position:absolute;left:14px;top:8px}
.welcome{left:0;top:267px;width:516px;height:171px;background:rgba(47,150,170,.7);padding:22px 0 0 20px;color:var(--white);font-weight:700;font-size:62px;line-height:68px;white-space:nowrap}
.hero-btn{top:516px;height:30px;background:#d7d7d7;color:#333;font-size:15px;font-weight:600;display:flex;align-items:center;justify-content:center}

/* party carousel */
.parties{top:830px;left:0;width:1200px;height:539px;background:var(--sky)}
.arrow{top:160px}
.card{top:18px;width:320px;text-align:center;color:var(--white)}
.card h3{font-size:24px;font-weight:700;height:28px;white-space:nowrap}
.card .photo{width:320px;height:269px;border:3px solid var(--white);margin-top:4px}
.card p{margin-top:18px;font-size:19px;line-height:21px;color:#0d3552;white-space:nowrap}
.btn{display:inline-flex;align-items:center;justify-content:center;width:116px;height:30px;font-size:15px;font-weight:600}
.card .btn{margin-top:12px;background:var(--white);color:var(--sky)}

/* strap */
.strap{top:1369px;left:0;width:1200px;height:183px;background:var(--sun);text-align:center;color:var(--white)}
.strap h2{margin-top:32px;font-size:36px;font-weight:700;letter-spacing:.5px;white-space:nowrap}
.strap p{font-size:25px;font-weight:600;margin-top:2px;white-space:nowrap}
.strap .btn{margin-top:12px;background:var(--white);color:var(--sun);height:33px}

/* news */
.news{top:1598px;left:0;width:1200px;height:598px;background:radial-gradient(ellipse at 50% 40%,#4a4a4a 0%,var(--dark-band) 70%)}
.news h2{position:absolute;top:50px;width:100%;text-align:center;color:var(--teal);font-size:80px;font-weight:400;letter-spacing:-1px;white-space:nowrap}
.story{top:225px;width:240px;text-align:center;color:var(--white)}
.story h3{color:var(--sun);font-size:34px;font-weight:400;white-space:nowrap}
.story p{margin-top:10px;font-size:15px;line-height:21px;font-weight:600;text-transform:uppercase}

/* features */
.feature{top:2256px;width:368px;text-align:center}
.feature h3{font-size:28px;font-weight:400;color:var(--teal);letter-spacing:-1px;height:46px;line-height:46px;white-space:nowrap}
.feature .photo{width:368px;height:274px;margin-top:3px}
.feature .btn{margin-top:30px;color:var(--white)}

/* sports */
.sports{top:2705px;left:0;width:1200px;height:666px;background:linear-gradient(180deg,#7b8aa3 0%,#56607a 35%,#3f4453 70%,#a34a4a 100%)}
.sports-box{left:347px;top:289px;width:544px;height:146px;background:rgba(43,160,200,.8);text-align:center;color:var(--white)}
.sports-box h2{margin-top:22px;font-size:50px;font-weight:600;letter-spacing:-.5px;white-space:nowrap}
.sports-box p{font-size:25px;font-weight:600;letter-spacing:7px;white-space:nowrap}

/* footer */
.site-footer{top:3434px;left:0;width:1200px;height:340px;background:var(--footer);color:var(--white)}
.col{top:50px}
.col h4{font-size:21px;font-weight:700;height:48px;white-space:nowrap}
.col li{list-style:none;font-size:19px;line-height:31px;white-space:nowrap}
.col .hl{color:var(--link-blue)}
.divider{top:52px;width:1px;height:240px;background:#5c5c5c}
.foot-brand{left:876px;top:150px;font-size:34px;font-weight:700;letter-spacing:1px;display:flex;align-items:center;gap:12px;white-space:nowrap}
.foot-brand i{display:block;width:22px;height:22px;background:var(--teal-light)}
</style>
</head>
<body>

<div class="abs social" aria-label="Social links"><span class="s1"></span><span class="s2"></span><span class="s3"></span></div>

<header class="abs site-header">
  <div class="abs brand"><i></i>BRACKMOOR HALLS</div>
  <div class="abs account-links">
    <span>GIFT VOUCHER</span> | <span class="on">JOIN OUR MAILING LIST</span> | <span>MY ACCOUNT</span> | <span>BASKET</span> | <span>REGISTER</span>
  </div>
  <div class="abs box-office">BOX OFFICE : 01632 960 482</div>
</header>

<nav class="abs main-nav">
  <a href="#">WHAT'S ON</a><a href="#">CONFERENCING &amp; EVENTS</a><a href="#">SPORTS &amp; LEISURE</a><a href="#" class="current">ROTUNDA THEATRE</a><a href="#">PLAN YOUR VISIT</a><a href="#">NEWS</a><a href="#">DISCOVER MORE</a><a href="#">CONTACT US</a>
</nav>

<section class="abs hero" role="img" aria-label="Guests mingling and talking at a networking reception with a buffet">
  <div class="abs search">
    <svg width="22" height="22" viewBox="0 0 22 22"><circle cx="9" cy="9" r="6.5" fill="none" stroke="#2bb4e8" stroke-width="2.5"/><line x1="14" y1="14" x2="20" y2="20" stroke="#2bb4e8" stroke-width="3"/></svg>
  </div>
  <div class="abs welcome">WELCOME TO<br>BRACKMOOR</div>
  <a class="abs hero-btn" style="left:911px;width:110px">MORE</a>
  <a class="abs hero-btn" style="left:1057px;width:115px">BOOCK</a>
</section>

<section class="abs parties">
  <svg class="abs arrow" style="left:40px" width="30" height="50" viewBox="0 0 30 50"><polyline points="24,6 6,25 24,44" fill="none" stroke="#fff" stroke-width="6"/></svg>
  <svg class="abs arrow" style="left:1134px" width="30" height="50" viewBox="0 0 30 50"><polyline points="6,6 24,25 6,44" fill="none" stroke="#fff" stroke-width="6"/></svg>

  <div class="abs card" style="left:89px">
    <h3>BIRTHDAY PARTIES</h3>
    <div class="photo" role="img" aria-label="Birthday cake with pink frosting" style="background:linear-gradient(135deg,#a8d8e4,#f2c4cf 55%,#7cc2d4)"></div>
    <p>Aenean nec eros luctus<br>Vestibulum ante faucibus orci<br>Ultrices posuere itudin<br>Suspendisse sollic velitaugue<br>Ut pharetra augue nec</p>
    <a class="btn">MORE</a>
  </div>
  <div class="abs card" style="left:441px">
    <h3>WEDDING PARTIES</h3>
    <div class="photo" role="img" aria-label="Wedding couple holding a bridal bouquet" style="background:linear-gradient(135deg,#6f9a3c,#2b2b2b 50%,#e9e2de)"></div>
    <p>Aenean nec eros luctus<br>Vestibulum ante faucibus orci<br>Ultrices posuere itudin<br>Suspendisse sollic velitaugue<br>Ut pharetra augue nec</p>
    <a class="btn">MORE</a>
  </div>
  <div class="abs card" style="left:796px">
    <h3>CORPORATE EVENTS</h3>
    <div class="photo" role="img" aria-label="Audience applauding a speaker at a corporate event" style="background:linear-gradient(135deg,#d97a3a,#7a2418 55%,#2a2f55)"></div>
    <p>Aenean nec eros luctus<br>Vestibulum ante faucibus orci<br>Ultrices posuere itudin<br>Suspendisse sollic velitaugue<br>Ut pharetra augue nec</p>
    <a class="btn">MORE</a>
  </div>
</section>

<section class="abs strap">
  <h2>WE ARE A LEADING EVENT SERVICE COMPANY,</h2>
  <p>HELPING TO PRODUCE THOUSANDS OF PARTIES</p>
  <a class="btn">MORE</a>
</section>

<section class="abs news">
  <h2>LATEST FROM BRACKMOOR</h2>
  <article class="abs story" style="left:130px"><h3>NEWS STORY 1</h3><p>Is simply dummy text of the printing and typesetting industry. Lorem Ipsum has been the industry's standard dummy text ever since the 1500s, when an unknown printer</p></article>
  <article class="abs story" style="left:480px"><h3>NEWS STORY 1</h3><p>Is simply dummy text of the printing and typesetting industry. Lorem Ipsum has been the industry's standard dummy text ever since the 1500s, when an unknown printer</p></article>
  <article class="abs story" style="left:830px"><h3>NEWS STORY 1</h3><p>Is simply dummy text of the printing and typesetting industry. Lorem Ipsum has been the industry's standard dummy text ever since the 1500s, when an unknown printer</p></article>
</section>

<div class="abs feature" style="left:35px">
  <h3>CONFERENCE AND EVENT</h3>
  <div class="photo" role="img" aria-label="Delegate with a laptop at a conference hall" style="background:linear-gradient(135deg,#1f3f6a,#b5663c 60%,#3b2a2a)"></div>
  <a class="btn" style="background:var(--teal)">MORE</a>
</div>
<div class="abs feature" style="left:418px">
  <h3>PARTIES AT BRACKMOOR</h3>
  <div class="photo" role="img" aria-label="Friends raising champagne glasses at a party" style="background:linear-gradient(135deg,#3a1e14,#c98a3c 50%,#6a3320)"></div>
  <a class="btn" style="background:var(--sun)">MORE</a>
</div>
<div class="abs feature" style="left:803px">
  <h3>CO-WORKING HUB</h3>
  <div class="photo" role="img" aria-label="Laptop on a desk in warm light" style="background:linear-gradient(135deg,#f1c98c,#b8895a 50%,#4a3a33)"></div>
  <a class="btn" style="background:var(--teal)">MORE</a>
</div>

<section class="abs sports" role="img" aria-label="Crowd of runners at the start of a road race">
  <div class="abs sports-box">
    <h2>SPORTS AND LEISURE</h2>
    <p>CLICK FOR MORE</p>
  </div>
</section>

<footer class="abs site-footer">
  <div class="abs col" style="left:50px"><h4>WHAT WE DO</h4><ul><li>Lacinia est</li><li>Proin dictum</li><li>Elementum velit</li><li>Consequat ante</li><li>Lorem ipsum dolor</li><li>Sit amet</li></ul></div>
  <div class="abs divider" style="left:254px"></div>
  <div class="abs col" style="left:342px"><h4 style="color:var(--link-blue)">OUR STORY</h4><ul><li>Lacinia est</li><li>Proin dictum</li><li>Elementum velit</li><li class="hl">Consequat ante</li><li>Lorem ipsum dolor</li><li>Sit amet</li></ul></div>
  <div class="abs divider" style="left:556px"></div>
  <div class="abs col" style="left:604px"><h4>CONTACTS</h4></div>
  <div class="abs foot-brand"><i></i>BRACKMOOR</div>
</footer>

</body>
</html>
```